Multiple Page Flyer -6 pager

Looking for an attractive new flyer for our synthetic greens and turf division. Please use our new logo attached and theme around the logo and use lots of pictures from the website. Pick the best from

I envision the following:
Page 1: Cover page
Page 2: Golfing Greens
Page 3: Golfing Greens 2
Page 4: Artificial Lawns 50% / Pet Turf 50%
Page 5: Pet Turf 50% / Playgrounds 50%
Page 6: Sports

```html
<!DOCTYPE html>
<html lang="en">
<head>
<meta charset="utf-8">
<title>Summit Turf Greens – Inside Spread</title>
<link rel="stylesheet" href="https://fonts.googleapis.com/css2?family=Marcellus&family=Montserrat:wght@800&family=Ubuntu:wght@400;500&display=swap">
<style>
  :root {
    --lime: #8cc63f;
    --white: #ffffff;
    --maroon: #7b3a34;
    --turf-dark: #3b2c1d;
    --turf-mid: #2c9a2f;
    --turf-bright: #3fc43d;
    --veil: rgba(255, 255, 255, 0.8);
    --page-bg: #e9e9e9;
  }
  * { box-sizing: border-box; margin: 0; padding: 0; }
  html, body { width: 1200px; height: 800px; overflow: hidden; background: var(--page-bg); }
  .spread { position: relative; width: 1200px; height: 800px; display: flex; }
  .green-photo {
    position: absolute; left: 0; top: 0; width: 800px; height: 800px;
    background:
      radial-gradient(ellipse 180px 60px at 520px 640px, rgba(255,255,255,0.55), transparent 70%),
      linear-gradient(180deg, var(--turf-dark) 0%, #4a3a22 18%, var(--turf-mid) 32%, var(--turf-bright) 70%, #34b236 100%);
  }
  .lawn-photo {
    position: absolute; left: 800px; top: 0; width: 400px; height: 800px;
    background: linear-gradient(125deg, #9fcf6a 0%, #5fae3a 35%, #4e8f33 60%, #7a6a55 80%, #8d7e6c 100%);
  }
  .panel { position: relative; width: 400px; height: 800px; padding: 0 40px; color: var(--white); font-family: "Ubuntu", sans-serif; }
  .panel + .panel { border-left: 1px solid rgba(0,0,0,0.12); }
  .section-tag {
    display: inline-block; background: var(--lime); color: var(--white);
    font-family: "Marcellus", serif; font-size: 19px; letter-spacing: 2px;
    padding: 8px 80px 6px 22px; margin-bottom: 14px;
  }
  .body-copy { font-size: 11.5px; line-height: 1.5; font-weight: 500; margin-bottom: 12px; text-shadow: 0 1px 2px rgba(0,0,0,0.3); }
  .putting { padding-top: 90px; }
  .ranges { margin-top: 46px; }
  .phone { position: absolute; left: 40px; bottom: 46px; display: flex; align-items: center; gap: 12px; font-size: 20px; font-weight: 500; letter-spacing: 1px; }
  .brand { display: flex; align-items: center; justify-content: center; gap: 8px; padding-top: 36px; margin-bottom: 22px; font-family: "Marcellus", serif; font-size: 20px; letter-spacing: 1px; }
  .brand-dot { width: 12px; height: 12px; border-radius: 50%; background: var(--white); }
  .tee-tag { margin-top: 18px; }
  .stats-card {
    position: absolute; left: 60px; top: 120px; width: 290px; height: 590px;
    background: var(--veil); color: var(--maroon); padding: 40px 28px; text-align: center;
  }
  .stat-label { font-family: "Marcellus", serif; font-size: 17px; letter-spacing: 2px; }
  .stat-value { font-family: "Montserrat", sans-serif; font-weight: 800; font-size: 70px; line-height: 1.05; }
  .stat-rule { border: 0; border-top: 2px solid var(--maroon); margin: 14px 0 22px; }
  .stats-copy { margin-top: 34px; font-family: "Ubuntu", sans-serif; font-size: 12.5px; line-height: 1.55; font-weight: 500; }
</style>
</head>
<body>
<main class="spread">
  <div class="green-photo" role="img" aria-label="Photo of a green putter and blue golf ball beside a hole on a synthetic putting green"></div>
  <div class="lawn-photo" role="img" aria-label="Photo of a roll of artificial lawn turf laid beside soil"></div>

  <section class="panel">
    <div class="putting">
      <h2 class="section-tag">PUTTING</h2>
      <p class="body-copy">Make no mistake: the design and installation of a synthetic turf putting green is both a science and an art. Not only should putting greens be visually striking, they should also be installed with the utmost precision and expertise to ensure a great golf game, time after time.</p>
      <p class="body-copy">Given the importance of a putting green to a flawless game, it's unwise to leave its design and installation to chance. At Summit Turf Greens, we use only the finest synthetic turf materials and construction methods to create your beautiful, signature golf green.</p>
    </div>
    <div class="ranges">
      <h2 class="section-tag">DRIVIN RANGERS</h2>
      <p class="body-copy">In southeastern Wisconsin where winters seem endless, it's no surprise that driving ranges are popular spots for fun and recreation year-round. Not only does practicing regularly at a driving range help significantly improve a golfer's technique, driving ranges also offer a relaxing respite from the hustle and bustle of daily life for lovers of the sport.</p>
      <p class="body-copy">At Summit Turf Greens, we don't just have a passion for creating beautiful landscapes, we also have a passion for golf too. We love the sport as equally as our customers and want to convey that with every project we do.</p>
      <p class="body-copy">So whether you're in the market for building the ultimate at-home driving range, or if you're a business person simply looking to capitalize on the popularity of golf by building your very own public driving range, Summit Turf Greens is here to help.</p>
    </div>
    <div class="phone">
      <svg width="30" height="30" viewBox="0 0 30 30" aria-hidden="true">
        <path d="M9 5 L13 10 L10.5 13 Q13 18 17 19.5 L20 17 L25 21 L22 25 Q12 25 5 12 Z" fill="none" stroke="var(--lime)" stroke-width="2" stroke-linejoin="round"/>
        <path d="M17 6 A8 8 0 0 1 24 13 M17 2 A12 12 0 0 1 28 13" fill="none" stroke="var(--lime)" stroke-width="2" stroke-linecap="round"/>
      </svg>
      <span>(555) 014-2290</span>
    </div>
  </section>

  <section class="panel">
    <div class="brand"><span class="brand-dot"></span><span>SUMMIT TURF GREENS</span></div>
    <p class="body-copy">Requiring less maintenance than real grass, our synthetic golf greens are built to last. Unlike competitors, our greens also look realistic, giving players the ultimate sensory experience of being on a freshly cut green and anticipating a long, successful day of play. But perhaps best of all, our driving range greens are installed with only the most expert construction techniques. So whether you're on year one or year fifty at your driving range, you can expect your green to function and look as beautiful as the day it was installed.</p>
    <h2 class="section-tag tee-tag">TEE BOXES</h2>
    <p class="body-copy">For the uninitiated, a tee box or teeing ground is the starting point on each hole on a course, situated between two tee markers and set back two-club-lengths. To many, the tee box is just another spot on the green. But for serious golfers and lovers of the sport, the tee box can represent many things, including both the excitement and anticipation of a new hole or fresh game. For this reason, the building of a tee box should always be left in the hands of a professional.</p>
    <p class="body-copy">At Summit Turf Greens, we're leaders in the design and installation of artificial golf greens, including putting greens and tee boxes. When you partner with us for your in-home or commercial tee-box, we're with you every step of the way.</p>
    <p class="body-copy">First, we start with design, creating accurate-to-scale images of your property that will give a clear picture of exactly what your design will look like fully built. Next, we focus on the build, tending to each step of the construction process with care, precision and sincere attention to detail. What's next? Tee up. No matter how big or small your project, once your tee box is installed, it's ready for your first tee time immediately. There's need for additional upkeep or maintenance. That's our promise to our customers, time after time.</p>
  </section>

  <section class="panel">
    <div class="stats-card">
      <p class="stat-label">ARTIFICIAL LAWNS</p>
      <p class="stat-value">50%</p>
      <hr class="stat-rule">
      <p class="stat-label">PET TRUF</p>
      <p class="stat-value">50%</p>
      <p class="stats-copy">We love our pets, and we can't imagine life without them. However, no one likes a yard full of bare or brown spots, and no one likes muddy paws tracking dirt and debris through the house. Many a pet owner has daydreamed about a life with a perfect lawn and their furry friend at their side. Now that dream can be a reality with beautiful, low maintenance pet lawns from Summit Turf Greens – your source for the best artificial lawn installation services in Milwaukee and the surrounding areas.</p>
    </div>
  </section>
</main>
</body>
</html>
```